Electrical needs letterhead design

Need a letterhead design for an electrical company. Using the same colours as to what are used in the logo.
After a modern design.

Want the logo in top right or top left.

Must include...

ABN 61 842 307 194
PHONE 0492357018
www.voltarnex.com.au
ben@voltarnex.com.au

'ABN' and 'PHONE' in bold.

Keep it basic. Logo top left, details either next to it or far right corner. Dont want any other objects included.

```html
<!DOCTYPE html>
<html lang="en">
<head>
<meta charset="utf-8">
<title>Voltarnex Letterhead</title>
<link rel="stylesheet" href="https://fonts.googleapis.com/css2?family=Open+Sans:wght@400;600;700&display=swap">
<style>
  :root {
    --canvas-bg: #e6e6e6;
    --paper: #ffffff;
    --brand-red: #9b1b1b;
    --ink: #1e1e1e;
    --ink-soft: #3a3a3a;
    --sig-tone: #cfcfcf;
  }
  html, body {
    margin: 0;
    padding: 0;
    width: 1200px;
    height: 1000px;
    overflow: hidden;
    background: var(--canvas-bg);
    font-family: "Open Sans", Arial, sans-serif;
    color: var(--ink);
  }
  .letterhead {
    position: absolute;
    left: 255px;
    top: 12px;
    width: 690px;
    height: 976px;
    background: var(--paper);
    box-shadow: 0 2px 10px rgba(0,0,0,0.12);
  }
  .brand {
    position: absolute;
    left: 100px;
    top: 74px;
    display: flex;
    align-items: center;
    gap: 8px;
  }
  .brand-dot {
    width: 14px;
    height: 14px;
    border-radius: 50%;
    background: var(--brand-red);
  }
  .brand-name {
    font-size: 36px;
    font-weight: 600;
    color: var(--brand-red);
    line-height: 1;
    letter-spacing: 0.2px;
  }
  .contact {
    position: absolute;
    right: 84px;
    top: 84px;
    text-align: right;
    font-size: 10.5px;
    line-height: 13px;
    color: var(--ink);
  }
  .contact b { font-weight: 700; }
  .subject {
    position: absolute;
    left: 192px;
    top: 238px;
    font-size: 12px;
    font-weight: 700;
  }
  .sender {
    position: absolute;
    right: 515px;
    top: 274px;
    text-align: right;
    font-size: 12px;
    line-height: 16.5px;
    color: var(--ink-soft);
  }
  .sender .sender-name { font-weight: 700; color: var(--ink); }
  .body-copy {
    position: absolute;
    left: 192px;
    top: 274px;
    width: 415px;
    font-size: 12px;
    line-height: 16.5px;
    text-align: justify;
    color: var(--ink);
  }
  .body-copy p { margin: 0 0 16.5px 0; }
  .signature-mark {
    position: absolute;
    left: 192px;
    top: 774px;
    width: 100px;
    height: 26px;
    background: linear-gradient(90deg, var(--sig-tone), #e8e8e8);
    border-radius: 3px;
  }
  .signature-caption {
    position: absolute;
    left: 192px;
    top: 804px;
    font-size: 9px;
    font-weight: 600;
  }
</style>
</head>
<body>
  <main class="letterhead">
    <header>
      <div class="brand">
        <span class="brand-dot"></span>
        <span class="brand-name">Voltarnex</span>
      </div>
      <address class="contact" style="font-style: normal;">
        <b>ABN</b> 61 842 307 194<br>
        <b>PHONE</b> 0492357018<br>
        www.voltarnex.com.au<br>
        ben@voltarnex.com.au
      </address>
    </header>

    <div class="subject">Lorem ipsum dolor sit amet, ei eros vidit sonet eum</div>

    <div class="sender">
      <span class="sender-name">Your Name</span><br>
      Function<br>
      Details Function<br>
      sed
    </div>

    <section class="body-copy">
      <p>Lorem ipsum dolor sit amet, ei eros vidit sonet eum, sed ea aliquam offendit. Reque quando labitur nec in, no solum ceteros est. Accumsan pertinacia an qui. Te vidisse recteque pro, cu per habemus officiis, eos ex malis posidonium omittantur. Appetere principes eloquentiam vis ei, an mea alia petentium dignissim, te justo omnium duo.</p>
      <p>Movet laoreet delicatissimi cum id. Essent dissentiet cu cum, atqui augue iriure qui ea. Liber propriae ei sed. Euismod ornatus scaevola et pro.</p>
      <p>Verterem interesset disputationi vim et, laudem persecuti quo eu. Mea viderer vulputate ut. Ad scripta scaevola appetere usu, omnium forensibus sed cu, dolorum admodum postulant mea ei. Eos ut ubique graeco insolens, etiam electram assentior cum at.</p>
      <p>In eos solum verterem facilisis, magna scaevola explicari has ex, at vidisse percipitur cum. At dicam postea luptatum sea, sed te timeam principes disputando, postea scaevola eloquentiam quo eu. Cetero concludaturque cu ius, nam erat detraxit ut, in his cetero vocent erroribus. Eu sint nulla comprehensam qui. Dolor dolorum splendide ei est, id usu inani liber deterruisset.</p>
      <p>Omnis intellegat intellegam duo cu, no ornatus partiendo referrentur has Verterem interesset disputationi vim et, laudem persecuti quo eu. Mea viderer vulputate ut. Ad scripta scaevola appetere usu, omnium forensibus sed cu, dolorum admodum postulant mea ei. Eos ut ubique graeco insolens, etiam electram assentior cum at.</p>
    </section>

    <div class="signature-mark" role="img" aria-label="Handwritten signature"></div>
    <div class="signature-caption">Your Name. CEO</div>
  </main>
</body>
</html>
```